Flyer für Handwerksunternehmen
Zielgruppe
Wir sind ein Handwerksunternehmen. Wir bieten alle Leistungen aus einer Hand. Mehr Infos unter www.werkbaukolleg.de
Aufgabenstellung
Modernes Design

```html
<!DOCTYPE html>
<html lang="de">
<head>
<meta charset="utf-8">
<title>Werkbaukolleg – Unsere Kompetenzen</title>
<link rel="stylesheet" href="https://fonts.googleapis.com/css2?family=Playfair+Display:wght@400&display=swap">
<style>
  :root {
    --bg: #1c1a1a;
    --band: #2c2b2b;
    --text: #ffffff;
    --icon: #d8d8d8;
    --brand: #5a595d;
  }
  html, body {
    margin: 0;
    padding: 0;
    overflow: hidden;
    background: var(--bg);
  }
  .flyer {
    position: relative;
    width: 928px;
    height: 1200px;
    overflow: hidden;
    background: var(--bg);
    font-family: "Playfair Display", Georgia, serif;
    color: var(--text);
  }
  .texture-band {
    position: absolute;
    inset: 0;
    width: 928px;
    height: 1200px;
  }
  .headline {
    position: absolute;
    top: 108px;
    left: 0;
    width: 928px;
    margin: 0;
    text-align: center;
    font-weight: 400;
    font-size: 31px;
    line-height: 41px;
    letter-spacing: 0.5px;
  }
  .competence-icon {
    position: absolute;
    background: var(--icon);
    border-radius: 10px;
  }
  .competence-label {
    position: absolute;
    margin: 0;
    text-align: center;
    font-size: 24px;
    line-height: 23px;
    text-transform: uppercase;
    white-space: nowrap;
    transform: translateX(-50%);
  }
  .competence-label.loose { line-height: 39px; }
  .claim {
    position: absolute;
    top: 680px;
    left: 0;
    width: 928px;
    margin: 0;
    text-align: center;
    font-size: 32px;
    line-height: 39.5px;
  }
  .brand-name {
    position: absolute;
    top: 960px;
    left: 0;
    width: 928px;
    margin: 0;
    text-align: center;
    font-size: 40px;
    line-height: 48px;
    font-weight: 400;
    color: var(--brand);
  }
</style>
</head>
<body>
<main class="flyer">
  <svg class="texture-band" viewBox="0 0 928 1200" role="img" aria-label="Diagonales Band mit dunkler Struktur und geschwungenen Linien">
    <polygon points="0,0 125,0 928,1035 928,1200 870,1200 0,95" fill="var(--band)"/>
  </svg>

  <h1 class="headline">UNSERE KOMPETENZEN<br>BAUMANAGEMENT VOM PROFI</h1>

  <div class="competence-icon" style="left:100px;top:243px;width:48px;height:87px" role="img" aria-label="Symbol Bauleiter mit Haus"></div>
  <p class="competence-label" style="left:252px;top:264px">Umfassende<br>Baubetreuung</p>

  <div class="competence-icon" style="left:484px;top:240px;width:74px;height:100px" role="img" aria-label="Symbol Deutschlandkarte mit Standortmarke"></div>
  <p class="competence-label loose" style="left:698px;top:254px">Deutschlandweit<br>tätig</p>

  <div class="competence-icon" style="left:76px;top:362px;width:82px;height:95px" role="img" aria-label="Symbol Fachmann mit fünf Sternen"></div>
  <p class="competence-label loose" style="left:252px;top:369px">Langjährige<br>Erfahrung</p>

  <div class="competence-icon" style="left:460px;top:362px;width:80px;height:74px" role="img" aria-label="Symbol Mitarbeitergruppe"></div>
  <p class="competence-label" style="left:700px;top:378px">Mitarbeiter aus allen<br>Handwerksbereichen</p>

  <div class="competence-icon" style="left:80px;top:491px;width:94px;height:96px" role="img" aria-label="Symbol vernetzte Partner"></div>
  <p class="competence-label" style="left:303px;top:517px">Umfangreiches<br>Partnernetzwerk</p>

  <div class="competence-icon" style="left:488px;top:491px;width:92px;height:96px" role="img" aria-label="Symbol Hände, die ein Team tragen"></div>
  <p class="competence-label" style="left:698px;top:517px">Alle Leistungen<br>aus einer Hand</p>

  <p class="claim">Vertrauen Sie uns die Ausführung Ihres<br>Bauprojektes an und profitieren Sie von<br>unserem erfahrenen Blick auf<br>Wirtschaftlichkeit und Qualität.</p>

  <p class="brand-name">Werkbaukolleg</p>
</main>
</body>
</html>
```